Update the A4 Specials Page for Restaurant/Cafe

Provide a MINIMALIST attractive Specials page we can print weekly for our food and drink specials to give to our guests. Final design is to be provided in WORD Document so it can be easily edited by Manager. Should be black text and MINIMALIST to minimise ink usage as we print hundreds a week. We have UPLOADED the existing page as a template for you to update. Maybe logo can stay, see what you think. Or delete it and do something else. Keep it simple. Choose a good FONT. Could be a little playful with a cocktail ICON or something. Our existing menus can be seen at www.tallpinebistro.com.au and they are using font Alegreya. Please note we are unable to provide any feedback to designers, however we really do appreciate your time if you are submitting a design. Thank you for your participation.

```html
<!DOCTYPE html>
<html lang="en">
<head>
<meta charset="utf-8">
<title>Tall Pine Bistro – Weekly Specials</title>
<link href="https://fonts.googleapis.com/css2?family=Berkshire+Swash&family=Montserrat:wght@600&display=swap" rel="stylesheet">
<style>
  :root {
    --mat: #c9c9cb;
    --paper: #ffffff;
    --ink: #111111;
    --ink-soft: #2a2a2a;
    --rule: #111111;
    --sketch: #f3f3f3;
    --ornament: #e4e4e4;
  }
  * { margin: 0; padding: 0; box-sizing: border-box; }
  html, body { width: 920px; height: 1200px; overflow: hidden; }
  body { background: var(--mat); position: relative; }

  .specials-page {
    position: absolute; left: 118px; top: 117px; width: 683px; height: 966px;
    background: var(--paper);
    overflow: hidden;
  }
  .brand-band {
    position: absolute; left: 0; top: 80px; width: 100%; height: 102px;
    border-top: 2px solid var(--rule); border-bottom: 2px solid var(--rule);
    display: flex; align-items: center; justify-content: center;
  }
  .brand-name {
    font-family: "Berkshire Swash", serif; font-size: 36px; color: var(--ink);
    letter-spacing: 1px;
  }

  .sketch { position: absolute; background: var(--sketch); border-radius: 40px; }
  .sketch--martini { left: 0; top: 203px; width: 158px; height: 226px; }
  .sketch--tumbler { left: 505px; top: 396px; width: 165px; height: 215px; }
  .sketch--wine { left: 0; top: 633px; width: 141px; height: 209px; }

  .special { position: absolute; left: 158px; width: 366px; }
  .special__head {
    display: flex; align-items: baseline; color: var(--ink);
    font-family: "Berkshire Swash", serif; font-size: 27px; line-height: 1;
  }
  .special__leader {
    flex: 1; margin: 0 5px; border-bottom: 2px dotted var(--ink); transform: translateY(-3px);
  }
  .special__desc {
    margin-top: 14px; color: var(--ink-soft);
    font-family: "Montserrat", sans-serif; font-weight: 600; font-size: 13.5px; line-height: 17px;
  }
  .special__desc p + p { margin-top: 4px; }
  .special__desc--list { margin-top: 20px; }
  .special__desc--list p + p { margin-top: 2.5px; }

  .special--filo { top: 275px; }
  .special--soup { top: 445px; }
  .special--cocktail { top: 579px; }
  .special--beer { top: 715px; }

  .ornament { position: absolute; background: var(--ornament); border-radius: 12px; }
  .ornament--left { left: 34px; top: 848px; width: 85px; height: 82px; }
  .ornament--right { left: 566px; top: 848px; width: 85px; height: 82px; }
  .footer-rule { position: absolute; left: 119px; top: 928px; width: 447px; border-bottom: 2px dotted var(--rule); }
</style>
</head>
<body>
  <main class="specials-page">
    <div class="sketch sketch--martini" role="img" aria-label="Faint line sketch of a margarita glass with citrus slice"></div>
    <div class="sketch sketch--tumbler" role="img" aria-label="Faint line sketch of an iced cocktail tumbler with mint and straw"></div>
    <div class="sketch sketch--wine" role="img" aria-label="Faint line sketch of a tilted wine glass with strawberry"></div>

    <header class="brand-band">
      <span class="brand-name">Tall Pine Bistro</span>
    </header>

    <section class="special special--filo">
      <div class="special__head"><span>Chicken Filo</span><span class="special__leader"></span><span>$24</span></div>
      <div class="special__desc">
        <p>Creamy Chicken with Pinenuts,<br>wrapped in Filo Pastry.</p>
        <p>Served with Side Salad &amp; Zulu Sauce</p>
      </div>
    </section>

    <section class="special special--soup">
      <div class="special__head"><span>Minestrone Soup</span><span class="special__leader"></span><span>$8</span></div>
      <div class="special__desc"><p>Served with Garlic Bread</p></div>
    </section>

    <section class="special special--cocktail">
      <div class="special__head"><span>Cocktail Special</span><span class="special__leader"></span><span>$17</span></div>
      <div class="special__desc"><p>PASSIONISTA</p></div>
    </section>

    <section class="special special--beer">
      <div class="special__head"><span>Craft Beer Special</span><span class="special__leader"></span><span>$10</span></div>
      <div class="special__desc special__desc--list">
        <p>CROOKED HERON</p>
        <p>CITRUS BURST</p>
        <p>Tropical Pale Ale</p>
        <p>4.8% Alc.</p>
      </div>
    </section>

    <div class="ornament ornament--left" role="img" aria-label="Flourish ornament, bottom left corner"></div>
    <div class="footer-rule"></div>
    <div class="ornament ornament--right" role="img" aria-label="Flourish ornament, bottom right corner"></div>
  </main>
</body>
</html>
```